Hero Image Redesign for VELM Consulting Website

About us:
VELM Consulting is an organisational psychology and human resource management consulting firm based in Melbourne, Australia (www.velmadvisory-example.com.au). We are a B2B offering a range of organisational psychology measurement and consulting. The largest part of our business is our online psychometric assessments, which are self-managed via an online portal, which is currently used by many organisations worldwide as part of their recruitment process.

What we are looking for:
We are seeking assistance to redesign an image located above the fold - on the top right hand side of homepage. We want an image of a small group of diverse people happily working together using a laptop (either individually or as a group), overlayed with graphic representations reflective of using our online Psychometric Assessment tool, in an interactive fashion.

The graphics will highlight key features of the self-service VELM Psychometric Assessment Portal, specifically ease of use, flexibility and our integrated approach. We want the image to look clean, clear, minimal, with use of negative space. All graphics must be accessible (including sufficient colour contrast and text size).

We would like the graphic to feature 3 “pop ups” highlighting features, and these should appear over the image:

1. Setup participants easily online
2. Check the status of an assessment
3. View participants’ reports

Examples from other SaaS websites attached.

The final design should communicate trust, reliability, our scientific evidence based approach, and our approachable and friendly customer service.

Our main brand colours are:
• Navy – HEX #2F2971
• Mid Blue – HEX #0C75C0
• Black – HEX #000000

About VELM’ website and potential for future work:

• VELM’ website pages have been created using Bricks Builder for WordPress.
• There is a strong possibility of future projects following successful delivery. We are an excellent client – ethical, professional and with a genuine commitment to partnership.

Need extra days to review

```html
<!DOCTYPE html>
<html lang="en">
<head>
<meta charset="utf-8">
<title>VELM Consulting — Organisational Psychology Consulting</title>
<link href="https://fonts.googleapis.com/css2?family=Plus+Jakarta+Sans:wght@400;500;600;700&family=Montserrat:ital,wght@1,300;1,700&display=swap" rel="stylesheet">
<style>
  :root {
    --navy: #2f2971;
    --navy-deep: #2e2a6e;
    --divider: #5a48d8;
    --teal: #a8e4df;
    --ink: #1f1f2b;
    --body: #4a4a52;
    --nav-bg: #f6f6f6;
    --white: #ffffff;
  }
  * { box-sizing: border-box; margin: 0; padding: 0; }
  html, body { width: 1200px; height: 626px; overflow: hidden; background: var(--white); }
  body { position: relative; font-family: "Plus Jakarta Sans", sans-serif; }

  .site-header {
    position: absolute; top: 0; left: 0; width: 1200px; height: 65px;
    background: var(--nav-bg);
  }
  .brand {
    position: absolute; left: 18px; top: 17px;
    display: flex; align-items: center; gap: 8px;
    font-size: 24px; font-weight: 700; color: var(--navy);
    letter-spacing: -0.3px;
  }
  .brand-mark { width: 22px; height: 22px; background: var(--teal); border-radius: 5px; }
  .main-nav { position: absolute; top: 0; left: 0; height: 65px; }
  .nav-item {
    position: absolute; top: 23px;
    font-size: 13px; font-weight: 500; color: var(--ink);
    display: flex; align-items: center; gap: 8px; white-space: nowrap;
  }
  .nav-item svg { width: 10px; height: 6px; }

  .hero-copy { position: absolute; left: 55px; top: 130px; }
  .hero-title {
    font-size: 64px; font-weight: 600; line-height: 70px;
    color: var(--navy-deep); letter-spacing: -0.5px;
  }
  .hero-lede {
    position: absolute; left: 55px; top: 372px; width: 520px;
    font-size: 22px; line-height: 40px; color: var(--body); font-weight: 400;
    letter-spacing: -0.2px;
  }
  .hero-actions { position: absolute; left: 54px; top: 506px; display: flex; gap: 37px; }
  .btn {
    width: 206px; height: 52px; border-radius: 3px;
    display: flex; align-items: center; justify-content: center; gap: 10px;
    font-size: 15.5px; font-weight: 700;
    box-shadow: 0 3px 6px rgba(0,0,0,0.12);
  }
  .btn-primary { background: var(--navy); color: var(--white); }
  .btn-secondary { background: var(--teal); color: var(--navy); }

  .hero-visual { position: absolute; left: 0; top: 0; width: 1200px; height: 626px; }

  .feature-text {
    position: absolute; font-family: "Montserrat", sans-serif; font-style: italic;
    color: var(--white); font-size: 27px; letter-spacing: -0.6px; white-space: nowrap;
  }
  .feature-text .light { font-weight: 300; }
  .feature-text .strong { font-weight: 700; }
  .feature-setup { left: 754px; top: 109px; line-height: 29px; }
  .feature-status { left: 754px; top: 191px; line-height: 24px; }
  .feature-reports { left: 758px; top: 271px; line-height: 30px; font-size: 24px; letter-spacing: -0.7px; }
</style>
</head>
<body>

<header class="site-header">
  <div class="brand"><span class="brand-mark"></span>VELM Consulting</div>
  <nav class="main-nav">
    <span class="nav-item" style="left:345px">Psychometric testing <svg viewBox="0 0 10 6"><path d="M1 1l4 4 4-4" fill="none" stroke="#1f1f2b" stroke-width="1.5"/></svg></span>
    <span class="nav-item" style="left:521px">Employee wellbeing <svg viewBox="0 0 10 6"><path d="M1 1l4 4 4-4" fill="none" stroke="#1f1f2b" stroke-width="1.5"/></svg></span>
    <span class="nav-item" style="left:691px">HR consulting <svg viewBox="0 0 10 6"><path d="M1 1l4 4 4-4" fill="none" stroke="#1f1f2b" stroke-width="1.5"/></svg></span>
    <span class="nav-item" style="left:821px">Events</span>
    <span class="nav-item" style="left:890px">Knowledge hub <svg viewBox="0 0 10 6"><path d="M1 1l4 4 4-4" fill="none" stroke="#1f1f2b" stroke-width="1.5"/></svg></span>
    <span class="nav-item" style="left:1032px">About us <svg viewBox="0 0 10 6"><path d="M1 1l4 4 4-4" fill="none" stroke="#1f1f2b" stroke-width="1.5"/></svg></span>
    <span class="nav-item" style="left:1132px">Contact</span>
  </nav>
</header>

<section class="hero-copy">
  <h1 class="hero-title">Organisational<br>Psychology<br>Consulting</h1>
</section>
<p class="hero-lede">Optimise your workforce with psychometric testing, engagement surveys, wellbeing measures and organisational development.</p>
<div class="hero-actions">
  <span class="btn btn-primary">Psychometric Testing</span>
  <span class="btn btn-secondary">Speak to an Expert
    <svg width="12" height="10" viewBox="0 0 12 10"><path d="M1 5h9M6.5 1.5L10 5l-3.5 3.5" fill="none" stroke="#2f2971" stroke-width="1.5"/></svg>
  </span>
</div>

<svg class="hero-visual" viewBox="0 0 1200 626">
  <defs>
    <linearGradient id="photoTones" x1="0" y1="0" x2="1" y2="1">
      <stop offset="0" stop-color="#d8c2a3"/>
      <stop offset="0.55" stop-color="#b39a84"/>
      <stop offset="1" stop-color="#8c7d72"/>
    </linearGradient>
  </defs>

  <path class="support-bubble" fill="var(--teal)"
        d="M744 374 H1063 Q1119 374 1119 430 V520 Q1119 560 1085 570 L1111 613 L1040 576 H744 Q688 576 688 520 V430 Q688 374 744 374 Z"/>

  <rect class="photo-area" x="688" y="330" width="372" height="248" rx="40"
        fill="url(#photoTones)" role="img"
        aria-label="Photo of three smiling colleagues working together around a laptop"/>

  <path class="features-bubble" fill="var(--navy)"
        d="M700 93 H1027 Q1122 93 1122 188 V241 Q1122 336 1027 336 H737 L615 381 L650 330 Q605 310 605 241 V188 Q605 93 700 93 Z"/>
  <line x1="634" y1="184" x2="1104" y2="184" stroke="var(--divider)" stroke-width="2"/>
  <line x1="650" y1="257" x2="1104" y2="257" stroke="var(--divider)" stroke-width="2"/>

  <g fill="none" stroke="#fff" stroke-width="2.2" stroke-linecap="round">
    <path d="M677 129 V124 H684 M711 124 H718 V129 M677 156 V161 H684 M711 161 H718 V156"/>
    <circle cx="697.5" cy="134" r="6"/>
    <path d="M687 155 Q687 144 697.5 144 Q708 144 708 155 Z"/>
    <circle cx="671" cy="140" r="4.5"/>
    <path d="M662 156 Q662 148 671 148 Q677 148 679 151"/>
    <circle cx="714" cy="140" r="4.5"/>
    <path d="M723 156 Q723 148 714 148 Q708 148 706 151"/>
  </g>

  <g fill="none" stroke="#fff" stroke-width="2.2" stroke-linecap="round" stroke-linejoin="round">
    <rect x="667" y="202" width="49" height="42" rx="4"/>
    <path d="M685 202 V198 Q685 196 688 196 H695 Q698 196 698 198 V202"/>
    <circle cx="679" cy="217" r="4.5"/><path d="M677 217 l1.5 1.5 3-3"/>
    <circle cx="679" cy="231" r="4.5"/><path d="M677 231 l1.5 1.5 3-3"/>
    <path d="M688 215 H708 M688 220 H704 M688 229 H708 M688 234 H704"/>
  </g>

  <g fill="none" stroke="#fff" stroke-width="2.2" stroke-linecap="round" stroke-linejoin="round">
    <path d="M670 275 H701 L708 282 V298 M708 316 V317 H670 Z"/>
    <path d="M676 290 H688 M676 297 H684 M676 304 H688"/>
    <circle cx="698" cy="298" r="8"/>
    <path d="M704 304 L718 317"/>
  </g>
</svg>

<div class="feature-text feature-setup"><span class="light">Setup </span><span class="strong">participants</span><br><span class="strong">easily online</span></div>
<div class="feature-text feature-status"><span class="light">Check the </span><span class="strong">status of</span><br><span class="strong">an assessment</span></div>
<div class="feature-text feature-reports"><span class="light">View </span><span class="strong">participants’ reports</span></div>

</body>
</html>
```